ZRD Roofing Billboard Design

Looking for a fresh new billboard design with my new headshot photo and using some info from my previous billboard and maybe website for design/content inspiration. My website is https://zrdroofing.com/

Also attached are my logo and current lawn sign design. I am looking for something simple, clean and modern. The landing page website should be 3816tops.com like my previous billboard has.

```html
<!DOCTYPE html>
<html lang="en">
<head>
<meta charset="utf-8">
<title>ZRD Roofing Billboard</title>
<link rel="stylesheet" href="https://fonts.googleapis.com/css2?family=Anton&family=Exo+2:ital,wght@0,700;0,800;1,800&family=Montserrat:wght@700&display=swap">
<style>
  :root {
    --navy: #1d3560;
    --navy-deep: #162a4c;
    --green: #8fa61f;
    --green-bright: #9bbf2c;
    --white: #ffffff;
    --backdrop: #dedede;
    --photo-top: #f4f6f8;
    --photo-mid: #c9d2e4;
    --photo-low: #b4c0da;
  }
  * { margin: 0; padding: 0; box-sizing: border-box; }
  html, body { width: 1021px; height: 1200px; overflow: hidden; background: var(--backdrop); }
  .billboard {
    position: absolute; left: 31px; top: 460px;
    width: 960px; height: 279px;
    background: var(--white); overflow: hidden;
  }
  .brand {
    position: absolute; left: 22px; top: 30px; width: 286px;
    display: flex; flex-direction: column; align-items: center; gap: 18px;
  }
  .brand-dot { width: 118px; height: 118px; border-radius: 50%; background: var(--green-bright); }
  .brand-name {
    font-family: "Montserrat", sans-serif; font-weight: 700;
    font-size: 26px; letter-spacing: 1px; color: var(--navy); white-space: nowrap;
  }
  .phone-band {
    position: absolute; left: 0; top: 225px; width: 313px; height: 54px;
    background: var(--navy-deep);
    display: flex; align-items: center; justify-content: center;
  }
  .phone {
    font-family: "Exo 2", sans-serif; font-weight: 800; font-style: italic;
    font-size: 30px; color: var(--white); letter-spacing: 1.5px; white-space: nowrap;
  }
  .web-band {
    position: absolute; left: 589px; top: 225px; width: 371px; height: 54px;
    background: var(--green);
    display: flex; align-items: center; justify-content: flex-end; padding-right: 26px;
  }
  .website {
    font-family: "Exo 2", sans-serif; font-weight: 800; font-style: italic;
    font-size: 36px; color: var(--white); letter-spacing: 2px; white-space: nowrap;
  }
  .headshot {
    position: absolute; left: 300px; top: 10px; width: 299px; height: 269px;
    background: linear-gradient(180deg, var(--photo-top) 0%, var(--photo-mid) 55%, var(--photo-low) 100%);
    border-radius: 120px 120px 0 0;
  }
  .headline {
    position: absolute; left: 599px; top: 10px; width: 350px;
    font-family: "Anton", sans-serif; font-weight: 400; color: var(--navy); line-height: 1;
    text-transform: uppercase; white-space: nowrap;
  }
  .headline .line-one { display: block; font-size: 74px; letter-spacing: 5px; }
  .headline .line-two { display: block; font-size: 58px; letter-spacing: 3px; margin-top: -4px; }
  .price-pill {
    position: absolute; left: 599px; top: 159px; width: 336px; height: 46px;
    border-radius: 23px; background: var(--navy-deep); overflow: hidden;
  }
  .price-label {
    position: absolute; left: 15px; top: 0; height: 46px; line-height: 46px;
    font-family: "Exo 2", sans-serif; font-weight: 800; font-size: 23px;
    letter-spacing: 0.5px; color: var(--white); white-space: nowrap;
  }
  .price-value {
    position: absolute; left: 156px; top: 0; width: 180px; height: 46px;
    border-radius: 23px; background: var(--green-bright);
    font-family: "Exo 2", sans-serif; font-weight: 800; font-size: 36px; letter-spacing: 1.5px;
    color: var(--white);
    display: flex; align-items: center; justify-content: center;
  }
  .price-value sup { font-size: 18px; margin-right: 2px; align-self: flex-start; margin-top: 4px; }
</style>
</head>
<body>
  <section class="billboard">
    <div class="brand">
      <div class="brand-dot"></div>
      <div class="brand-name">ZRD Roofing LLC</div>
    </div>

    <div class="phone-band"><span class="phone">(555) 201-7730</span></div>

    <div class="headshot" role="img" aria-label="Headshot of the company owner, smiling, in a light blue shirt"></div>

    <h1 class="headline">
      <span class="line-one">Full Roof</span>
      <span class="line-two">Replacement</span>
    </h1>

    <div class="price-pill">
      <span class="price-label">Starting @</span>
      <span class="price-value"><sup>$</sup>7,499</span>
    </div>

    <div class="web-band"><span class="website">3816TOPS.COM</span></div>
  </section>
</body>
</html>
```